Letter Head for accounting firm

We need letter head designed using our attached logo.

We also need the following information on the letterhead:

482 E Mill Rd. Danvers, OH 43762

HarborLedgerLtd.com

1-855-613-2907

Contact Information for Business Card

Use logo

Colors

Designer to choose colors to be used in the design.

Requirements
Must have
• Business Card - Should also have name and title - email address

```html
<!DOCTYPE html>
<html lang="en">
<head>
<meta charset="utf-8">
<title>Harbor Ledger Group – Business Card</title>
<link href="https://fonts.googleapis.com/css2?family=Montserrat:wght@700&family=Lato:wght@400&display=swap" rel="stylesheet">
<style>
  :root {
    --brand-blue: #1479c0;
    --brand-dark: #262b33;
    --panel-white: #f7f8f9;
    --hex-white: #f2f3f4;
    --ink: #2f3338;
    --page-bg: #e8e9eb;
  }
  html, body {
    margin: 0;
    padding: 0;
    width: 1200px;
    height: 900px;
    overflow: hidden;
    background: var(--page-bg);
  }
  .business-card {
    position: absolute;
    left: 100px;
    top: 140px;
    width: 1000px;
    height: 620px;
    box-shadow: 0 10px 30px rgba(0,0,0,0.18);
    overflow: hidden;
    font-family: "Lato", Arial, sans-serif;
  }
  .card-shapes {
    position: absolute;
    inset: 0;
  }
  .holder {
    position: absolute;
    right: 60px;
    top: 62px;
    text-align: right;
    color: #ffffff;
  }
  .holder-name {
    font-family: "Montserrat", Arial, sans-serif;
    font-weight: 700;
    font-size: 34px;
    letter-spacing: 0.5px;
    line-height: 40px;
    margin: 0;
  }
  .holder-title {
    font-size: 26px;
    line-height: 32px;
    margin: 0;
  }
  .contact-list {
    position: absolute;
    right: 62px;
    top: 262px;
    margin: 0;
    padding: 0;
    list-style: none;
    text-align: right;
    color: var(--ink);
    font-size: 27px;
    line-height: 36px;
  }
  .contact-list li {
    display: flex;
    justify-content: flex-end;
    align-items: center;
    gap: 10px;
  }
  .contact-icon {
    width: 20px;
    height: 20px;
    flex: none;
  }
  .address {
    position: absolute;
    right: 64px;
    top: 486px;
    margin: 0;
    text-align: right;
    color: #ffffff;
    font-size: 27px;
    line-height: 37px;
    font-style: normal;
  }
  .brand {
    position: absolute;
    left: 52px;
    top: 183px;
    width: 448px;
    height: 253px;
    display: flex;
    flex-direction: column;
    align-items: center;
    justify-content: center;
    gap: 16px;
  }
  .brand-square {
    width: 46px;
    height: 46px;
    background: var(--brand-blue);
  }
  .brand-name {
    font-family: "Montserrat", Arial, sans-serif;
    font-weight: 700;
    font-size: 30px;
    line-height: 36px;
    color: var(--brand-blue);
    text-align: center;
    margin: 0;
  }
</style>
</head>
<body>
  <div class="business-card">
    <svg class="card-shapes" width="1000" height="620" viewBox="0 0 1000 620" aria-hidden="true">
      <rect class="panel-white" x="0" y="0" width="1000" height="620" fill="var(--panel-white)"/>
      <path class="band-blue" d="M0 0 H1000 V186 H500 V305 H0 Z" fill="var(--brand-blue)"/>
      <path class="band-dark" d="M0 305 H500 V434 H1000 V620 H0 Z" fill="var(--brand-dark)"/>
      <polygon class="brand-hexagon" points="276,54 500,183 500,436 276,566 52,436 52,183" fill="var(--hex-white)"/>
    </svg>

    <div class="brand">
      <div class="brand-square"></div>
      <p class="brand-name">HARBOR LEDGER<br>GROUP LTD</p>
    </div>

    <div class="holder">
      <p class="holder-name">DANIEL HARTWELL</p>
      <p class="holder-title">Managing Director</p>
    </div>

    <ul class="contact-list">
      <li>1-855-613-2907
        <svg class="contact-icon" viewBox="0 0 20 20" aria-hidden="true"><path d="M3 6c0-2 3-3 7-3s7 1 7 3v2h-4V6.5c-2-.6-4-.6-6 0V8H3z M5 10h10l2 7H3z" fill="var(--brand-blue)"/></svg>
      </li>
      <li>info@HarborLedgerLtd.com
        <svg class="contact-icon" viewBox="0 0 20 20" aria-hidden="true"><rect x="2" y="4" width="16" height="12" fill="var(--brand-blue)"/><path d="M2 4l8 7 8-7" fill="none" stroke="#fff" stroke-width="1.5"/></svg>
      </li>
      <li>www.HarborLedgerLtd.com
        <svg class="contact-icon" viewBox="0 0 20 20" aria-hidden="true"><circle cx="10" cy="10" r="8" fill="var(--brand-blue)"/><path d="M6 7c2 0 2 2 4 2s1 3 0 4 M12 5c1 1 2 1 3 2" fill="none" stroke="#fff" stroke-width="1.4"/></svg>
      </li>
    </ul>

    <address class="address">482 E Mill Rd.<br>Danvers, OH 43762</address>
  </div>
</body>
</html>
```